Business card design needed for a security services business.

We provide a wide range of security services from guard personnel to electronic systems.

Industry/Entity Type

Security Industry

Contact Information for Business Card

Brent Holloway, Owner Office: 780.555.0148; Cell: 780.555.0193 Email: brent@korvanshieldgroup.example; Address 20417 163 St Edmonton, AB T5X 2K8

Colors
0054AA
0677BA
7BADD7
CADEEF
E8F1F8

Requirements
Nice to have
• On the back of the card I would like to possible list the services I provide: Guards Mobiles Live Video Surveillance Access Intrusion

```html
<!DOCTYPE html>
<html lang="en">
<head>
<meta charset="utf-8">
<title>Korvan Shield Group – Business Card</title>
<link rel="stylesheet" href="https://fonts.googleapis.com/css2?family=Montserrat:wght@400;500;700&display=swap">
<style>
  :root {
    --brand-deep: #0054AA;
    --brand-blue: #0677BA;
    --brand-sky: #7BADD7;
    --brand-mist: #CADEEF;
    --brand-ice: #E8F1F8;
    --ink: #3a3a3a;
    --rule-grey: #7a7a7a;
    --paper: #ffffff;
    --backdrop: #c9c9c9;
  }
  * { box-sizing: border-box; margin: 0; padding: 0; }
  html, body { width: 1200px; height: 788px; overflow: hidden; }
  body {
    background: var(--backdrop);
    font-family: "Montserrat", Arial, sans-serif;
    position: relative;
  }
  .card {
    position: absolute;
    left: 302px;
    width: 596px;
    height: 340px;
    border-radius: 22px;
    overflow: hidden;
    box-shadow: 0 6px 18px rgba(0,0,0,0.18);
  }
  .card--front { top: 36px; background: var(--paper); }
  .card--back { top: 412px; background: linear-gradient(135deg, var(--brand-blue), var(--brand-deep)); }

  .front-swoosh { position: absolute; inset: 0; width: 100%; height: 100%; }

  .wordmark {
    position: absolute;
    left: 40px;
    top: 112px;
    width: 210px;
    display: flex;
    align-items: center;
    gap: 10px;
    color: var(--brand-blue);
    font-weight: 700;
    font-size: 22px;
    line-height: 1.15;
    text-transform: uppercase;
    letter-spacing: 0.5px;
  }
  .wordmark__square {
    flex: none;
    width: 16px; height: 16px;
    background: var(--brand-blue);
  }

  .divider {
    position: absolute;
    left: 272px;
    top: 50px;
    width: 1px;
    height: 150px;
    background: var(--brand-blue);
  }

  .contact {
    position: absolute;
    left: 292px;
    top: 36px;
    color: var(--ink);
  }
  .contact__name {
    color: var(--brand-blue);
    font-weight: 700;
    font-size: 21px;
    line-height: 1.2;
    text-transform: uppercase;
    letter-spacing: 0.5px;
  }
  .contact__title { font-size: 13px; line-height: 1.3; margin-top: 2px; }
  .contact__address { font-size: 12px; line-height: 1.35; margin-top: 6px; }
  .contact__list { list-style: none; margin-top: 5px; font-size: 12px; line-height: 1.5; }
  .contact__list li { display: flex; align-items: center; gap: 7px; }
  .contact__list svg { width: 10px; height: 10px; flex: none; fill: var(--brand-blue); }

  .back-field { position: absolute; inset: 0; }
  .back-name {
    position: absolute;
    right: 50px;
    top: 86px;
    color: var(--paper);
    font-weight: 700;
    font-size: 24px;
    text-transform: uppercase;
    letter-spacing: 1px;
  }
  .services {
    position: absolute;
    left: 0; right: 0;
    bottom: 46px;
    display: flex;
    justify-content: center;
    gap: 26px;
    list-style: none;
    color: var(--paper);
    font-size: 15px;
    font-weight: 500;
    letter-spacing: 0.3px;
  }
  .services li::before { content: "•"; margin-right: 5px; }
</style>
</head>
<body>

<section class="card card--front" aria-label="Card front">
  <svg class="front-swoosh" viewBox="0 0 596 340" preserveAspectRatio="none" aria-hidden="true">
    <path d="M0 304 Q370 296 596 246 L596 340 L0 340 Z" fill="var(--brand-blue)"/>
    <path d="M0 296 Q370 288 596 236" fill="none" stroke="var(--rule-grey)" stroke-width="4"/>
  </svg>

  <div class="wordmark">
    <span class="wordmark__square"></span>
    <span>Korvan Shield Group</span>
  </div>

  <div class="divider"></div>

  <div class="contact">
    <h1 class="contact__name">Brent Holloway</h1>
    <p class="contact__title">Owner</p>
    <p class="contact__address">20417 163 St Edmonton<br>AB T5X 2K8</p>
    <ul class="contact__list">
      <li><svg viewBox="0 0 10 10"><path d="M2 0.5 L3.6 2.6 L2.7 3.7 Q4 6 6.3 7.3 L7.4 6.4 L9.5 8 L8.4 9.5 Q3 9 0.5 1.6 Z"/></svg>780.555.0148</li>
      <li><svg viewBox="0 0 10 10"><path d="M2.5 0 H7.5 V10 H2.5 Z M3.5 1 V8 H6.5 V1 Z"/></svg>780.555.0193</li>
      <li><svg viewBox="0 0 10 10"><path d="M0 2 H10 V8.5 H0 Z M0.8 2.6 L5 5.6 L9.2 2.6"/></svg>brent@korvanshieldgroup.example</li>
      <li><svg viewBox="0 0 10 10"><circle cx="5" cy="5" r="4.5"/></svg>www.korvanshieldgroup.example</li>
    </ul>
  </div>
</section>

<section class="card card--back" aria-label="Card back">
  <div class="back-field" role="img" aria-label="Repeating company initials pattern in darker blue across the card"></div>
  <p class="back-name">Korvan Shield Group</p>
  <ul class="services">
    <li>Guards Mobiles Live</li>
    <li>Video Surveillance</li>
    <li>Access Intrusion</li>
  </ul>
</section>

</body>
</html>
```